Redesign Event Flyer for Speaker

We are re-designing our professional event flyer template with new headshot and cleaner, up-to-date design. All design details are in PDF file attached. Thank you for participating :)

Font styles to use
Sans Serif

Colors
3276b5
0355a3

Requirements
Must have
• All elements in PDF file.
Nice to have
Should not have
• Tacky or childish elements.

```html
<!DOCTYPE html>
<html lang="en">
<head>
<meta charset="utf-8">
<title>The Greatest Sale – Event Flyer</title>
<link rel="stylesheet" href="https://fonts.googleapis.com/css2?family=Cinzel:wght@400&family=Oswald:wght@300;400;500;600&display=swap">
<style>
  :root {
    --blue-light: #3276b5;
    --blue-main: #0355a3;
    --blue-top: #0a5db3;
    --blue-deep: #05245f;
    --brand-red: #d62232;
    --white: #ffffff;
    --photo-suit: #1d2f57;
    --photo-skin: #6a4433;
  }
  * { margin: 0; padding: 0; box-sizing: border-box; }
  html, body { width: 1200px; height: 800px; overflow: hidden; }
  body { background: var(--blue-main); }

  .flyer {
    position: relative;
    width: 1200px;
    height: 800px;
    overflow: hidden;
    background: linear-gradient(180deg, var(--blue-top) 0%, var(--blue-main) 45%, #043f88 72%, var(--blue-deep) 100%);
    font-family: "Oswald", sans-serif;
    color: var(--white);
  }

  .speaker-photo {
    position: absolute;
    left: 60px;
    top: 55px;
    width: 650px;
    height: 745px;
    border-radius: 260px 260px 0 0;
    background: linear-gradient(180deg, var(--photo-skin) 0%, var(--photo-skin) 38%, #e9ecef 42%, var(--photo-suit) 55%, var(--photo-suit) 100%);
    opacity: 0.9;
  }

  .sponsor-brand {
    position: absolute;
    left: 700px;
    top: 34px;
    display: flex;
    align-items: center;
    gap: 12px;
  }
  .sponsor-brand .mark {
    width: 30px;
    height: 30px;
    background: var(--brand-red);
  }
  .sponsor-brand .name {
    font-family: "Oswald", sans-serif;
    font-weight: 600;
    font-size: 34px;
    line-height: 1;
    color: var(--brand-red);
  }

  .speaker-name {
    position: absolute;
    left: 602px;
    top: 143px;
    font-family: "Cinzel", serif;
    font-weight: 400;
    font-size: 24px;
    letter-spacing: 0.5px;
    color: var(--white);
  }

  .event-panel {
    position: absolute;
    left: 601px;
    top: 193px;
    width: 599px;
    height: 404px;
    background: linear-gradient(90deg, rgba(50,118,181,0.95) 0%, rgba(50,118,181,0.75) 45%, rgba(50,118,181,0) 100%);
    border-left: 7px solid var(--white);
    padding: 24px 0 0 32px;
  }
  .event-title {
    font-weight: 500;
    text-transform: uppercase;
    line-height: 1;
  }
  .event-title span { display: block; }
  .event-title .line-the { font-size: 58px; }
  .event-title .line-greatest { font-size: 78px; margin-top: 6px; }
  .event-title .line-sale { font-size: 100px; margin-top: 8px; }

  .event-date {
    margin-top: 30px;
    font-weight: 400;
    font-size: 20px;
  }
  .event-date sup { font-size: 11px; }
  .event-rule {
    width: 242px;
    height: 1px;
    background: var(--white);
    margin: 14px 0 12px;
  }
  .event-links {
    list-style: none;
    font-weight: 400;
    font-size: 21px;
    line-height: 25px;
  }

  .venue {
    position: absolute;
    left: 785px;
    top: 630px;
  }
  .venue-brand {
    display: flex;
    align-items: center;
    gap: 10px;
    margin-bottom: 22px;
  }
  .venue-brand .mark {
    width: 40px;
    height: 40px;
    border-radius: 50%;
    background: var(--white);
  }
  .venue-brand .name {
    font-weight: 500;
    font-size: 22px;
    line-height: 1;
  }
  .venue-address {
    font-style: normal;
    font-weight: 300;
    font-size: 19px;
    line-height: 29px;
  }
</style>
</head>
<body>
  <main class="flyer">
    <div class="speaker-photo" role="img" aria-label="Portrait of the speaker smiling, wearing a navy suit and white shirt"></div>

    <div class="sponsor-brand">
      <span class="mark"></span>
      <span class="name">Signcrest</span>
    </div>

    <h2 class="speaker-name">Marcus Daniel Whitfield</h2>

    <section class="event-panel">
      <h1 class="event-title">
        <span class="line-the">The</span>
        <span class="line-greatest">Greatest</span>
        <span class="line-sale">Sale</span>
      </h1>
      <p class="event-date">Friday, August 9<sup>th</sup>, 2019</p>
      <div class="event-rule"></div>
      <ul class="event-links">
        <li>marcusdanielwhitfield.com</li>
        <li>signcrest.ca</li>
      </ul>
    </section>

    <section class="venue">
      <div class="venue-brand">
        <span class="mark"></span>
        <span class="name">Rolling Falls Golf Club</span>
      </div>
      <address class="venue-address">
        4200 Riverside Pkwy,<br>
        Lakeview, Canada
      </address>
    </section>
  </main>
</body>
</html>
```